Stationary Design for Real Estate Brokerage

We need a stationary design package for an existing real estate brokerage in Chicago. We are looking for a modern, urban look and feel. We need the following pieces created business cards, note cards (4" x 6"), presentation folders, #10 envelope (4.125" x 9.5"), catalog envelope ( 9" x 12"), letterhead. I have included our current logo and color codes as well as some pieces that we like the look and feel of. Who ever wins this contest will be our go to designer. We have multiple projects coming up asap, multipage brochure, additional folders, sell sheets etc. Thanks for looking.

Target Market(s)

Upscale urban professionals

Industry/Entity Type

Real Estate

Font styles to use
Sans Serif

Requirements
Must have
• If photos are used they must be black and white or washed in the cyan color from our logo

```html
<!DOCTYPE html>
<html lang="en">
<head>
<meta charset="utf-8">
<title>Loftline Stationery Suite</title>
<link href="https://fonts.googleapis.com/css2?family=Open+Sans:wght@300;400;600&display=swap" rel="stylesheet">
<style>
  :root {
    --cyan: #1ba6e1;
    --cyan-soft: #6cc6ee;
    --paper: #ffffff;
    --ink: #5a5a5a;
    --ink-light: #9a9a9a;
    --stage: #e4e4e4;
    --shadow: rgba(0,0,0,0.12);
    --crease: #e6e6e6;
  }
  * { box-sizing: border-box; margin: 0; padding: 0; }
  html, body { width: 698px; height: 1200px; overflow: hidden; }
  body {
    background: var(--stage);
    font-family: "Open Sans", Arial, sans-serif;
    color: var(--ink);
    position: relative;
  }
  .sheet {
    position: absolute;
    background: var(--paper);
    box-shadow: 0 1px 4px var(--shadow);
    overflow: hidden;
  }
  .wordmark {
    color: var(--cyan);
    font-weight: 300;
    letter-spacing: 0.08em;
    white-space: nowrap;
    line-height: 1;
  }

  /* Letterhead front */
  .letterhead { left: 30px; top: 22px; width: 318px; height: 460px; }
  .letterhead .head-band {
    position: absolute; left: 90px; right: 0; top: 22px; height: 8px; background: var(--cyan);
  }
  .letterhead .wordmark { position: absolute; left: 16px; top: 19px; font-size: 13px; }
  .letter-body {
    position: absolute; left: 22px; right: 40px; top: 58px;
    font-size: 4.6px; line-height: 1.55; color: var(--ink);
  }
  .letter-body p { margin-bottom: 6px; }
  .letter-body .signature { display: block; width: 48px; height: 14px; margin: 4px 0 2px; }
  .letter-footer {
    position: absolute; left: 16px; right: 16px; bottom: 14px;
    border-top: 1px solid var(--cyan); padding-top: 4px;
    font-size: 4.2px; color: var(--ink-light);
    display: flex; justify-content: space-between; white-space: nowrap;
  }

  /* Letterhead back */
  .letterhead-back { left: 360px; top: 22px; width: 318px; height: 460px; }
  .letterhead-back .top-band {
    position: absolute; left: 0; right: 0; top: 22px; height: 8px; background: var(--cyan);
  }
  .letterhead-back .wordmark {
    position: absolute; left: 0; right: 0; top: 198px; text-align: center; font-size: 26px;
  }
  .letterhead-back .site {
    position: absolute; right: 16px; bottom: 14px; font-size: 5px; color: var(--cyan);
  }

  /* Envelopes */
  .envelope-back { left: 30px; top: 500px; width: 318px; height: 138px; }
  .envelope-back svg { position: absolute; left: 0; top: 0; }
  .envelope { left: 30px; top: 652px; width: 318px; height: 138px; }
  .envelope .head-band {
    position: absolute; left: 88px; right: 0; top: 14px; height: 7px; background: var(--cyan);
  }
  .envelope .wordmark { position: absolute; left: 12px; top: 11px; font-size: 12px; }
  .envelope .return {
    position: absolute; left: 12px; top: 28px; font-size: 4.2px; color: var(--ink-light); line-height: 1.5;
  }

  /* Business cards */
  .card { width: 150px; height: 86px; left: 440px; }
  .card-front { top: 522px; }
  .card-front .head-band {
    position: absolute; left: 0; right: 0; top: 0; height: 6px; background: var(--cyan);
  }
  .card-front .name {
    position: absolute; left: 10px; top: 16px; font-size: 6px; font-weight: 600; color: var(--cyan);
  }
  .card-front .title { position: absolute; left: 10px; top: 24px; font-size: 4.4px; color: var(--ink-light); }
  .card-front .details {
    position: absolute; left: 10px; top: 44px; font-size: 4.2px; line-height: 1.6; color: var(--ink);
    white-space: nowrap;
  }
  .card-back { top: 632px; }
  .card-back .wordmark { position: absolute; left: 0; right: 0; top: 36px; text-align: center; font-size: 14px; }
  .card-back .foot-band {
    position: absolute; left: 0; right: 0; bottom: 0; height: 5px; background: var(--cyan);
  }

  /* Folder cover */
  .folder-cover { left: 30px; top: 806px; width: 300px; height: 378px; }
  .folder-cover .top-band {
    position: absolute; left: 0; right: 0; top: 26px; height: 10px; background: var(--cyan);
  }
  .folder-cover .wordmark {
    position: absolute; left: 0; right: 0; top: 150px; text-align: center; font-size: 26px;
  }
  .folder-cover .site {
    position: absolute; left: 16px; bottom: 14px; font-size: 5px; color: var(--cyan);
  }

  /* Folder inside */
  .folder-inside { left: 360px; top: 806px; width: 318px; height: 378px; background: var(--cyan); }
  .folder-inside .ghost-mark {
    position: absolute; right: 14px; top: 28px; font-size: 38px; font-weight: 300;
    letter-spacing: 0.08em; color: var(--cyan-soft); line-height: 1; white-space: nowrap;
  }
  .folder-inside .pocket {
    position: absolute; left: 0; right: 0; bottom: 0; height: 180px; background: var(--paper);
    border-top: 1px solid #dcdcdc;
  }
  .folder-inside .card-slot {
    position: absolute; left: 150px; top: 200px; width: 120px; height: 68px;
    background: var(--paper); box-shadow: 0 1px 3px var(--shadow);
  }
  .card-slot .head-band { position: absolute; left: 0; right: 0; top: 0; height: 5px; background: var(--cyan); }
  .card-slot .name { position: absolute; left: 8px; top: 13px; font-size: 5px; font-weight: 600; color: var(--cyan); }
  .card-slot .details {
    position: absolute; left: 8px; top: 24px; font-size: 3.8px; line-height: 1.6; color: var(--ink);
    white-space: nowrap;
  }
</style>
</head>
<body>

  <section class="sheet letterhead">
    <div class="head-band"></div>
    <div class="wordmark">LOFTLINE</div>
    <div class="letter-body">
      <p>March 14, 2024</p>
      <p>Ms. Dana Hollis<br>Director<br>Harlow &amp; Finch Co.<br>410 North Avenue<br>Chicago, IL 60610</p>
      <p>Dear Ms. Hollis,</p>
      <p>Thank you for meeting with our team last week to discuss your plans for the new residential project. We were pleased to learn more about your goals, and we believe our experience in downtown properties makes us a strong partner for every stage of the process ahead.</p>
      <p>Enclosed you will find a summary of recent sales in the neighborhood, along with our proposed marketing schedule and a short overview of the services our brokerage provides.</p>
      <p>We look forward to working with you and will follow up early next week.</p>
      <p>Sincerely,</p>
      <svg class="signature" viewBox="0 0 48 14" aria-hidden="true">
        <path d="M2 10 C8 2, 12 12, 18 6 S28 4, 30 9 S40 5, 46 7" fill="none" stroke="#555" stroke-width="0.8"/>
      </svg>
      <p>Adrian Kole<br>Principal Broker</p>
    </div>
    <div class="letter-footer">
      <span>120 West Lake Street, Chicago, IL 60601</span>
      <span>T 312 555 0148</span>
      <span>hello@loftlinehomes.com</span>
    </div>
  </section>

  <section class="sheet letterhead-back">
    <div class="top-band"></div>
    <div class="wordmark">LOFTLINE</div>
    <div class="site">loftlinehomes.com</div>
  </section>

  <section class="sheet envelope-back">
    <svg width="318" height="138" viewBox="0 0 318 138" aria-hidden="true">
      <polygon points="0,0 318,0 159,70" fill="var(--cyan)"/>
      <polyline points="0,138 159,80 318,138" fill="none" stroke="var(--crease)" stroke-width="1"/>
    </svg>
  </section>

  <section class="sheet envelope">
    <div class="head-band"></div>
    <div class="wordmark">LOFTLINE</div>
    <div class="return">120 West Lake Street<br>Chicago, IL 60601</div>
  </section>

  <section class="sheet card card-front">
    <div class="head-band"></div>
    <div class="name">Adrian Kole</div>
    <div class="title">Principal Broker</div>
    <div class="details">
      T 312 555 0148<br>
      adrian@loftlinehomes.com<br>
      120 West Lake Street, Chicago, IL 60601
    </div>
  </section>

  <section class="sheet card card-back">
    <div class="wordmark">LOFTLINE</div>
    <div class="foot-band"></div>
  </section>

  <section class="sheet folder-cover">
    <div class="top-band"></div>
    <div class="wordmark">LOFTLINE</div>
    <div class="site">loftlinehomes.com</div>
  </section>

  <section class="sheet folder-inside">
    <div class="ghost-mark">LOFTLINE</div>
    <div class="pocket"></div>
    <div class="card-slot">
      <div class="head-band"></div>
      <div class="name">Adrian Kole</div>
      <div class="details">
        Principal Broker<br>
        T 312 555 0148<br>
        adrian@loftlinehomes.com
      </div>
    </div>
  </section>

</body>
</html>
```